Business marketing flyer for mortgage company

I have a draft attached (DRAFT Manufactured flyer 3) with the contents of the flyer and a sample from a previous company I worked at. Need a flyer to promote our construction loans. attached is our company logo and the color codes. Note the sail on the company logo... would be cool if this could be incorporated into the flyer design.

```html
<!DOCTYPE html>
<html lang="en">
<head>
<meta charset="utf-8">
<title>Construction Loans Flyer</title>
<link href="https://fonts.googleapis.com/css2?family=Poppins:wght@400;500;600;700;800&display=swap" rel="stylesheet">
<style>
:root{
  --navy:#2b4a6f;
  --navy-dark:#223d5e;
  --cyan:#4fd8e6;
  --teal:#2a9fa9;
  --ink:#1d1d1f;
  --paper:#ffffff;
  --soft:#f1f3f5;
  --photo-a:#d9cfc4;
  --photo-b:#b98a5e;
}
*{box-sizing:border-box;margin:0;padding:0}
html,body{width:904px;height:1200px;overflow:hidden;background:var(--paper)}
body{font-family:'Poppins',sans-serif;color:var(--ink);position:relative}

.header{position:absolute;left:0;top:0;width:904px;height:170px;background:var(--navy);text-align:center;padding-top:34px}
.header-title{font-size:74px;font-weight:800;color:var(--cyan);letter-spacing:1px;line-height:1}
.header-sub{font-size:25px;font-weight:500;color:var(--cyan);letter-spacing:1.5px;margin-top:8px}

.hero{position:absolute;left:0;top:170px;width:904px;height:320px;background:var(--soft)}
.hero-photo{position:absolute;left:380px;top:0;width:524px;height:320px;
  background:linear-gradient(135deg,var(--photo-a),var(--photo-b));
  clip-path:polygon(0 0,100% 0,100% 100%,150px 100%)}
.hero-edge{position:absolute;left:0;top:0;width:904px;height:320px}
.brand{position:absolute;left:44px;top:56px;display:flex;align-items:center;gap:10px}
.brand-mark{width:22px;height:22px;background:var(--teal)}
.brand-name{font-size:26px;font-weight:700;color:var(--navy);letter-spacing:.5px}
.hero-intro{position:absolute;left:44px;top:118px;width:380px;font-size:24px;font-weight:500;line-height:1.28}

.band{position:absolute;left:0;width:904px;background:var(--navy);color:var(--paper);font-weight:700;text-align:center}
.band-financing{top:490px;height:68px;font-size:27px;line-height:68px;text-align:left;padding-left:60px}
.band-cta{top:958px;height:70px;font-size:30px;line-height:70px;letter-spacing:.5px}

.benefits{position:absolute;left:44px;top:590px;width:480px;list-style:none}
.benefits li{position:relative;padding-left:24px;font-size:17px;line-height:1.32;margin-bottom:4px}
.benefits li::before{content:"";position:absolute;left:2px;top:5px;border-left:13px solid var(--teal);border-top:8px solid transparent;border-bottom:8px solid transparent}

.apply{position:absolute;left:560px;top:540px;width:310px;background:var(--teal);border-radius:16px;color:var(--paper);text-align:center;padding:14px 16px 14px}
.apply-title{font-size:29px;font-weight:800;line-height:1.05}
.apply-step{margin-top:6px}
.apply-tag{display:inline-flex;align-items:center;gap:5px;background:var(--navy);padding:1px 10px;border-radius:3px;font-size:11px;font-weight:700;line-height:16px}
.apply-tag svg{width:11px;height:11px}
.apply-text{font-size:12px;font-weight:500;line-height:1.25;margin-top:2px}

.rates{position:absolute;left:44px;top:782px;border-collapse:collapse}
.rates th{font-size:17px;font-weight:600;padding:4px 0;text-align:center}
.rates th.row-label{font-size:12px;font-weight:700;text-align:left;width:200px;padding-right:16px;line-height:1.2}
.rates td{width:198px;height:54px;border:3px solid var(--navy);text-align:center;font-size:18px;font-weight:500}
.rates thead th{border:none}

.contact{position:absolute;display:flex;align-items:center;gap:18px}
.contact-left{left:44px;top:1050px}
.contact-right{right:40px;top:1046px;flex-direction:row-reverse;text-align:right}
.avatar{width:118px;height:118px;border-radius:50%;border:5px solid var(--navy);background:linear-gradient(160deg,#cfd8e3,#8aa3c0);flex:none}
.contact-name{font-size:17px;font-weight:800;color:var(--navy)}
.contact-role{font-size:12px;font-weight:500;color:var(--teal);line-height:1.1}
.contact-info{font-size:11.5px;line-height:1.35}
.contact-info b{color:var(--teal);font-weight:500}
.contact-web{font-size:11.5px;margin-top:8px}
.address{position:absolute;right:40px;top:1172px;font-size:11.5px}
</style>
</head>
<body>

<header class="header">
  <h1 class="header-title">CONSTRUCTION LOANS</h1>
  <p class="header-sub">FOR MANUFACTURED AND MODULAR HOMES</p>
</header>

<section class="hero">
  <div class="hero-photo" role="img" aria-label="Photo of a smiling family sitting among moving boxes in a new home"></div>
  <svg class="hero-edge" viewBox="0 0 904 320" aria-hidden="true">
    <polygon points="366,0 380,0 530,320 516,320" fill="var(--navy)"/>
  </svg>
  <div class="brand"><span class="brand-mark"></span><span class="brand-name">KEELWATER FINANCIAL</span></div>
  <p class="hero-intro">Keelwater Financial now offers One-Time and Two-Time Close Loans, allowing for more options and flexibility</p>
</section>

<div class="band band-financing">Available for FHA, VA, and Conventional Financing</div>

<ul class="benefits">
  <li>Land equity or gifts allowed for down payment</li>
  <li>Purchase of land can be rolled into the loan if not already owned</li>
  <li>Primary Residence, Second Home, or Investment Properties</li>
  <li>Competitive interest rates and fees</li>
  <li>You only work with construction loan specialists</li>
</ul>

<aside class="apply">
  <h2 class="apply-title">3 EASY WAYS<br>TO APPLY</h2>
  <div class="apply-step">
    <span class="apply-tag">1.
      <svg viewBox="0 0 24 24"><path fill="currentColor" d="M6.6 10.8a15.1 15.1 0 0 0 6.6 6.6l2.2-2.2a1 1 0 0 1 1-.25 11.4 11.4 0 0 0 3.6.57 1 1 0 0 1 1 1V20a1 1 0 0 1-1 1A17 17 0 0 1 3 4a1 1 0 0 1 1-1h3.5a1 1 0 0 1 1 1c0 1.25.2 2.45.57 3.57a1 1 0 0 1-.25 1z"/></svg>
      CALL</span>
    <p class="apply-text">555-010-xxxx or 555-014-2280</p>
  </div>
  <div class="apply-step">
    <span class="apply-tag">2.
      <svg viewBox="0 0 24 24"><circle cx="12" cy="12" r="9" fill="none" stroke="currentColor" stroke-width="2"/><path d="M3 12h18M12 3c3 3 3 15 0 18M12 3c-3 3-3 15 0 18" fill="none" stroke="currentColor" stroke-width="1.6"/></svg>
      ONLINE</span>
    <p class="apply-text">buildloanexample.com</p>
  </div>
  <div class="apply-step">
    <span class="apply-tag">3.
      <svg viewBox="0 0 24 24"><path d="M5 3h10l4 4v14H5z" fill="none" stroke="currentColor" stroke-width="2"/></svg>
      REQUEST</span>
    <p class="apply-text">Complete Pre-Approval Request<br>(See back page)</p>
  </div>
</aside>

<table class="rates">
  <thead>
    <tr><th class="row-label"></th><th>FHA</th><th>CONVENTIONAL</th><th>VA</th></tr>
  </thead>
  <tbody>
    <tr><th class="row-label">MINIMUM FICO SCORES</th><td>640</td><td>640</td><td>640</td></tr>
    <tr><th class="row-label">DOWN PAYMENT<br>AMOUNT</th><td>As low as 3.5%</td><td>As low as 5%</td><td>100% Financing</td></tr>
  </tbody>
</table>

<div class="band band-cta">CALL OR EMAIL TODAY FOR MORE INFORMATION!</div>

<div class="contact contact-left">
  <div class="avatar" role="img" aria-label="Portrait photo of the senior mortgage consultant"></div>
  <div>
    <p class="contact-name">EVAN HOLLOWAY</p>
    <p class="contact-role">Sr. Mortgage Consultant</p>
    <p class="contact-info">NMLS#: 10042 | CA-DOC10042<br>
      <b>O:</b> 555-013-1501 <b>M:</b> 555-016-4681<br>
      <b>F:</b> 555-018-7423<br>
      Evan.Holloway@keelwaterfin.com</p>
    <p class="contact-web">EvanHollowayHomes.com</p>
  </div>
</div>

<div class="contact contact-right">
  <div class="avatar" role="img" aria-label="Portrait photo of the builder sales manager"></div>
  <div>
    <p class="contact-name">GRANT MERCER</p>
    <p class="contact-role">Builder Sales Manager</p>
    <p class="contact-info">NMLS#: 2045518 | CA-DBO2045518<br>
      <b>M:</b> 555-014-2280<br>
      <b>F:</b> 555-017-4678<br>
      Grant.Mercer@keelwaterfin.com</p>
  </div>
</div>
<p class="address">4820 Harbor View Rd, Suite 110, Bayside, CA 90000</p>

</body>
</html>
```